Tidewell Gearworks LLC

We Need a business card design for a boat/car mechanic. Our thinking is to have Maybe a car on left side of card, boat on the right side of card and diagnostic computer in the middle and a cool creative way to connect all three together. We are also open to other ideas as well!
Would like for back of business card to have the contact info on it “Dorian Vellacott, text is best as the contact method 803-555-0192”

```html
<!DOCTYPE html>
<html lang="en">
<head>
<meta charset="utf-8">
<title>Tidewell Gearworks LLC – Business Card</title>
<link rel="stylesheet" href="https://fonts.googleapis.com/css2?family=Michroma&family=Exo+2:ital,wght@0,400;1,600&family=Saira:wght@600&display=swap">
<style>
  :root {
    --page-bg: #161616;
    --card-black: #0a0b0d;
    --card-edge: #2a2b2e;
    --electric-blue: #1e63ff;
    --deep-blue: #0a2a7a;
    --silver: #c9ccd2;
    --white: #f4f6fa;
    --gold: #d9b777;
    --gold-deep: #9b7632;
    --muted: #c8ccd4;
  }
  * { box-sizing: border-box; margin: 0; padding: 0; }
  html, body { width: 1200px; height: 1059px; overflow: hidden; background: var(--page-bg); }
  .canvas { position: relative; width: 1200px; height: 1059px; }

  .card {
    position: absolute; left: 247px; width: 706px;
    border-radius: 22px; overflow: hidden;
    background: radial-gradient(ellipse at 50% 45%, #15171c 0%, var(--card-black) 70%);
    box-shadow: 0 14px 30px rgba(0,0,0,.55);
  }
  .card-front { top: 81px; height: 403px; }
  .card-back  { top: 546px; height: 400px; }
  .card-swoosh { position: absolute; inset: 0; width: 100%; height: 100%; }

  .brand-name {
    position: absolute; top: 62px; left: 0; width: 100%;
    text-align: center; font-family: "Michroma", sans-serif;
    font-size: 27px; color: var(--white); letter-spacing: .5px;
  }
  .brand-rule {
    position: absolute; top: 102px; left: 130px; width: 446px; height: 1px;
    background: linear-gradient(90deg, transparent, var(--electric-blue), transparent);
  }
  .brand-tagline {
    position: absolute; top: 110px; left: 0; width: 100%;
    text-align: center; font-family: "Exo 2", sans-serif; font-style: italic;
    font-weight: 600; font-size: 20px; color: var(--electric-blue); letter-spacing: .3px;
  }
  .hero-art {
    position: absolute; top: 140px; left: 12px; width: 682px; height: 150px;
    border-radius: 10px;
    background:
      radial-gradient(ellipse at 50% 50%, rgba(40,110,255,.55) 0%, rgba(20,60,170,.25) 30%, transparent 60%),
      linear-gradient(90deg, #07090f 0%, #0d1a3d 25%, #0a1430 50%, #0d1a3d 75%, #07090f 100%);
  }
  .feature-row {
    position: absolute; top: 298px; left: 0; width: 100%;
    display: flex; justify-content: center; align-items: center; gap: 14px;
    font-family: "Exo 2", sans-serif; font-size: 8.5px; line-height: 11px;
    color: var(--muted); text-transform: uppercase;
  }
  .feature { display: flex; align-items: center; gap: 8px; }
  .feature svg { width: 22px; height: 22px; }
  .feature-divider { width: 1px; height: 22px; background: var(--electric-blue); }

  .contact-name {
    position: absolute; top: 124px; left: 0; width: 100%; text-align: center;
    font-family: "Michroma", sans-serif; font-size: 28px; color: var(--gold);
  }
  .contact-rule {
    position: absolute; top: 180px; left: 266px; width: 174px; height: 2px;
    background: linear-gradient(90deg, transparent, var(--gold-deep) 20%, #ffcc66 50%, var(--gold-deep) 80%, transparent);
  }
  .contact-phone {
    position: absolute; top: 192px; left: 0; width: 100%; text-align: center;
    font-family: "Saira", sans-serif; font-weight: 600; font-size: 36px;
    letter-spacing: 2px; color: var(--gold);
  }
</style>
</head>
<body>
<main class="canvas">

  <section class="card card-front">
    <svg class="card-swoosh" viewBox="0 0 706 403" preserveAspectRatio="none" aria-hidden="true">
      <path d="M470 0 Q650 30 706 140 L706 0 Z" fill="#1c1d21"/>
      <path d="M470 0 Q650 30 706 140" fill="none" stroke="var(--silver)" stroke-width="4"/>
      <path d="M440 2 Q630 40 700 150" fill="none" stroke="var(--electric-blue)" stroke-width="5"/>
      <path d="M0 290 Q120 390 260 403 L0 403 Z" fill="#1c1d21"/>
      <path d="M0 290 Q120 390 260 403" fill="none" stroke="var(--silver)" stroke-width="4"/>
      <path d="M4 265 Q130 380 290 403" fill="none" stroke="var(--electric-blue)" stroke-width="5"/>
    </svg>

    <h1 class="brand-name">TIDEWELL GEARWORKS LLC</h1>
    <div class="brand-rule"></div>
    <p class="brand-tagline">AUTO/MARINE DIAGNOSTICS AND REPAIR</p>

    <div class="hero-art" role="img" aria-label="Black sports sedan on the left and a speedboat with twin outboard motors on the right, linked by a red pulse line to a rugged diagnostic laptop in a glowing blue ring at the centre"></div>

    <div class="feature-row">
      <div class="feature">
        <svg viewBox="0 0 24 24" fill="none" stroke="var(--electric-blue)" stroke-width="1.6" aria-hidden="true">
          <circle cx="12" cy="12" r="8"/><circle cx="12" cy="12" r="3.5"/><circle cx="12" cy="12" r="1" fill="var(--electric-blue)"/>
          <path d="M12 1v5M12 18v5M1 12h5M18 12h5"/>
        </svg>
        <span>Accurate<br>Diagnostics</span>
      </div>
      <div class="feature-divider"></div>
      <div class="feature">
        <svg viewBox="0 0 24 24" fill="var(--electric-blue)" aria-hidden="true">
          <path d="M20.5 3.5a5 5 0 0 0-6.3 6.2L3 20.9 4.9 22.8 16 11.6a5 5 0 0 0 6.2-6.3l-3 3-2.4-.6-.6-2.4z"/>
        </svg>
        <span>Expert<br>Solutions</span>
      </div>
      <div class="feature-divider"></div>
      <div class="feature">
        <svg viewBox="0 0 24 24" fill="none" stroke="var(--electric-blue)" stroke-width="1.8" aria-hidden="true">
          <path d="M5 3h4l2 5-2.5 1.5a11 11 0 0 0 6 6L16 13l5 2v4a2 2 0 0 1-2 2A17 17 0 0 1 3 5a2 2 0 0 1 2-2z"/>
          <path d="M14 3a7 7 0 0 1 7 7M14 6.5a3.5 3.5 0 0 1 3.5 3.5"/>
        </svg>
        <span>Text for more<br>information</span>
      </div>
    </div>
  </section>

  <section class="card card-back">
    <svg class="card-swoosh" viewBox="0 0 706 400" preserveAspectRatio="none" aria-hidden="true">
      <path d="M430 0 Q640 30 706 280 L706 0 Z" fill="#1e1f22"/>
      <path d="M430 0 Q640 30 706 280" fill="none" stroke="var(--gold)" stroke-width="5"/>
      <path d="M0 190 Q40 360 260 400 L0 400 Z" fill="#1e1f22"/>
      <path d="M0 190 Q40 360 260 400" fill="none" stroke="var(--gold)" stroke-width="5"/>
    </svg>
    <h2 class="contact-name">Dorian Vellacott</h2>
    <div class="contact-rule"></div>
    <p class="contact-phone">803-555-0192</p>
  </section>

</main>
</body>
</html>
```